yard sign for lawncare business

I need a lawn sign design. ...The sign will be 18"X27"....it will be displayed with the 27" running horizontally. ...i need the company name and logo to be included and the same color as the graphic in the included file.....i also want the slogan included as well as the phone number 312-555-0186...all wording and numbers should be large and easy to see from passing cars on the road.....feel free to play around with background colors and wording and number placement

Ok guys....downloads are now available for viewing. ..sorry about the delay....thanks for your help and good luck

Business

```html
<!DOCTYPE html>
<html lang="en">
<head>
<meta charset="utf-8">
<title>TurfKeepers Yard Sign</title>
<link rel="stylesheet" href="https://fonts.googleapis.com/css2?family=Oswald:wght@600;700&family=Roboto:wght@700&display=swap">
<style>
  :root {
    --page: #ffffff;
    --frame: #0d0d0d;
    --brand-green: #4cb24c;
    --band-green: #345c05;
    --rule-grey: #8a8c8e;
    --grass-light: #8fd33a;
    --grass-mid: #5fa81c;
    --name-green: #e2f5c6;
    --phone-fill: #eef1e4;
    --phone-edge: #2a2a2a;
    --slogan: #ffffff;
  }
  * { box-sizing: border-box; margin: 0; padding: 0; }
  html, body { width: 1200px; height: 801px; overflow: hidden; background: var(--page); }
  .sign {
    position: absolute; left: 63px; top: 40px; width: 1074px; height: 720px;
    background: var(--frame); padding: 15px;
  }
  .sign-face { position: relative; width: 100%; height: 100%; background: var(--page); overflow: hidden; }
  .brand-name {
    position: absolute; top: 92px; left: 0; width: 100%; text-align: center;
    font-family: "Oswald", "Arial Narrow", sans-serif; font-weight: 700;
    font-size: 98px; line-height: 1; letter-spacing: 2px; color: var(--brand-green);
    text-transform: uppercase;
  }
  .slogan-band {
    position: absolute; top: 234px; left: 0; width: 100%; height: 66px;
    background: var(--band-green);
    border-top: 4px solid var(--rule-grey); border-bottom: 4px solid var(--rule-grey);
    display: flex; align-items: center; justify-content: center;
  }
  .slogan {
    font-family: "Roboto", Arial, sans-serif; font-weight: 700; font-size: 23px;
    color: var(--slogan); letter-spacing: 0.3px;
  }
  .grass {
    position: absolute; top: 315px; left: 0; width: 100%; height: 115px;
    background: linear-gradient(to bottom, #ffffff 0%, var(--grass-light) 30%, var(--grass-mid) 70%, var(--band-green) 100%);
  }
  .contact-panel {
    position: absolute; top: 430px; left: 0; width: 100%; bottom: 0; background: var(--band-green);
  }
  .contact-name {
    position: absolute; top: 445px; left: 0; width: 100%; text-align: center;
    font-family: "Oswald", "Arial Narrow", sans-serif; font-weight: 700; font-size: 70px;
    line-height: 1; color: var(--name-green);
  }
  .contact-phone {
    position: absolute; top: 530px; left: 0; width: 100%; text-align: center;
    font-family: "Oswald", "Arial Narrow", sans-serif; font-weight: 700; font-size: 124px;
    line-height: 1; letter-spacing: 3px; color: var(--phone-fill);
    -webkit-text-stroke: 3px var(--phone-edge); paint-order: stroke fill;
  }
</style>
</head>
<body>
  <div class="sign">
    <div class="sign-face">
      <div class="brand-name">TurfKeepers</div>
      <div class="slogan-band">
        <p class="slogan">WHEN YOUR GRASS GETS TALL, GIVE US A CALL.</p>
      </div>
      <div class="contact-panel"></div>
      <div class="grass" role="img" aria-label="Illustrated row of tall green grass blades"></div>
      <div class="contact-name">Dale Hutton</div>
      <div class="contact-phone">(312) 555-0186</div>
    </div>
  </div>
</body>
</html>
```